We would like a Industrial brouchure design, for OIL and Gas and chemical industry , target customers are Petrochemical refineries, power plants and Petroleum tanker trucks.
this brouchure should have product photos of our main products.
I.E - stainless steel expasnion joints, rubber expansion joints, Fabric expansion joints, Composite hose, hand built rubber hose.
this brouchure is to hand to customers to show them our company capabilities
Design ideas can be taken from our web site - www.korvanite.com.au
Our products are high end engineered products, we supply all of Australia, new Zealand and south east asia and pacific islands
i would like a location map on the brouchure showing our locations.
our locations are -

Perth Western Australia
Port hedland western Australia
Darwin Northen territory
Adelaide - south Australia
Brisbane - Queensland - Australia
Auckland - New zealnd
Singapore
Surabaya - Indonesia
jakarta - indonesia
Ho Chi Min City - Vietnam
balikpapan - indonesia

our comapny logo colors are Black and grey

we would need product photos as well for the following products

Composite hose
stainless steel expansion joints
rubber expasnion joints
Fabric expansion joints
hand biuilt rubber hose
Composite ship to shore petroleum dock hose
stainless braided flexible hose

Target Market(s)

petrochemical industry
refineries, petroleum tanker, power plants, mining

Requirements
Must have
• product photos
• map of where we are located
• high end company impression
Nice to have
• 3 plus pages

```html
<!DOCTYPE html>
<html lang="en">
<head>
<meta charset="utf-8">
<title>Korvanite Brochure Spread</title>
<link href="https://fonts.googleapis.com/css2?family=Roboto:ital,wght@0,400;0,500;0,700;1,700&display=swap" rel="stylesheet">
<style>
  :root{
    --stage:#2a2a2c;
    --paper:#f1f2f6;
    --ink:#2b2d33;
    --ink-soft:#4a4d55;
    --rule:#4b4d53;
    --tab:#55575d;
    --band:#1d1f24;
    --panel:rgba(236,238,244,0.86);
  }
  *{box-sizing:border-box;margin:0;padding:0}
  html,body{width:1200px;height:789px;overflow:hidden;background:var(--stage);font-family:"Roboto",sans-serif;color:var(--ink)}
  .spread{position:absolute;left:0;top:0;width:1200px;height:789px;display:flex}
  .page{position:relative;width:600px;height:789px;background:var(--paper);overflow:hidden}
  .page--left{box-shadow:inset -24px 0 28px -20px rgba(0,0,0,.28)}
  .page--right{box-shadow:inset 24px 0 28px -20px rgba(0,0,0,.22)}

  .photo{position:absolute;left:0;top:0;width:600px}
  .photo--tanker{height:410px;background:linear-gradient(160deg,#3c4a66 0%,#7d7f8c 35%,#e6a25c 55%,#b35a2a 70%,#2c2e36 100%)}
  .photo--refinery{height:440px;background:linear-gradient(180deg,#4f86c4 0%,#8fb5dd 45%,#9aa3ad 65%,#4f5660 85%,#2f343b 100%)}
  .photo-band{position:absolute;left:0;width:600px;height:36px;background:var(--band)}

  .intro-panel{position:absolute;left:42px;top:34px;width:300px;height:250px;background:var(--panel);padding:22px 22px}
  .intro-title{font-weight:700;font-size:17px;line-height:1.15;text-align:center;margin-bottom:12px}
  .intro-text{font-size:9.5px;line-height:1.42;text-align:justify;color:var(--ink-soft)}

  .content{position:absolute;left:40px;top:445px;width:345px}
  .content h2{font-weight:700;font-style:italic;font-size:13px;margin:0 0 5px}
  .content p{font-size:8.6px;line-height:1.4;color:var(--ink-soft);margin-bottom:16px;text-align:justify}

  .thumb{position:absolute;left:405px;width:150px;height:82px;border-radius:12px;border:3px solid #fff;box-shadow:0 2px 6px rgba(0,0,0,.25)}
  .thumb--plant{top:520px;background:linear-gradient(180deg,#2f3f78 0%,#c76a52 45%,#2a3550 100%)}
  .thumb--pump{top:612px;background:linear-gradient(135deg,#d9dce2 0%,#8d949e 45%,#2f5aa8 75%,#3a3f48 100%)}

  .footer-rule{position:absolute;left:0;top:0;width:600px;height:789px;pointer-events:none}
  .url-tab{position:absolute;top:730px;height:26px;width:150px;background:var(--tab);border-radius:13px;color:#fff;font-size:10px;letter-spacing:.5px;display:flex;align-items:center;justify-content:center}
  .page--left .url-tab{left:330px}
  .page--right .url-tab{left:400px}

  .brand{position:absolute;left:40px;top:475px;display:flex;align-items:center;gap:12px}
  .brand-dot{width:46px;height:46px;border-radius:50%;background:var(--ink-soft)}
  .brand-name{font-weight:700;font-size:24px;color:var(--ink-soft)}

  .product-list{position:absolute;left:40px;top:555px}
  .product-list h3{font-weight:700;font-size:13px;margin-bottom:8px}
  .product-list ul{list-style:none}
  .product-list li{font-weight:700;font-size:12px;line-height:1.35;padding-left:12px;position:relative}
  .product-list li::before{content:"";position:absolute;left:0;top:5px;border-left:6px solid var(--ink);border-top:3.5px solid transparent;border-bottom:3.5px solid transparent}

  .product-photo{position:absolute;left:360px;top:520px;width:200px;height:150px;border-radius:8px;background:radial-gradient(ellipse at 50% 50%,#d6d9de 0%,#9ea3aa 55%,#e7e9ec 100%)}
</style>
</head>
<body>
<main class="spread">
  <section class="page page--left">
    <div class="photo photo--tanker" role="img" aria-label="Photo of a petroleum tanker truck on a road at sunset with a refinery behind"></div>
    <div class="photo-band" style="top:398px"></div>
    <div class="intro-panel">
      <h1 class="intro-title">Fluid Transfer<br>Products Asia Pacific</h1>
      <p class="intro-text">Recognised as the trusted industry leader, Korvanite specialises in a range of flexible fluid transfer products which we supply throughout Australia and the South East Asia region. We have over 70 years of combined industry experience in manufacturing and fabricating products for demanding applications. Quality products and dependable customer service are supported by a dedicated team of specialists with proven knowledge, ready to deliver high quality products and service.</p>
    </div>
    <div class="content">
      <h2>Fluid Transfer Solutions</h2>
      <p>We pride ourselves on being flexible and are relentless in finding solutions for you in order to meet your requirements. At Korvanite we put you first. Our business is efficiently structured so that we can react quickly, be innovative and provide a reliable fluid transfer solution in a time frame that helps you. Our technical consultants will work with you to determine the requirements and come up with a cost effective solution that improves your operating systems.</p>
      <h2>Servicing the entire Asia Pacific region</h2>
      <p>Our extensive experience throughout countries such as Indonesia, Vietnam, and Singapore sets us apart from our competitors. This enables us to supply and support the entire Australian and Asia region.</p>
      <h2>Quality Service, Experience, and Knowledge</h2>
      <p>Korvanite has an outstanding team with more than 70 years' combined industry experience. Our team understands your needs and can determine the best solution for you. Our highly trained and qualified staff provide high quality service every time.</p>
    </div>
    <div class="thumb thumb--plant" role="img" aria-label="Photo of an industrial plant lit at dusk"></div>
    <div class="thumb thumb--pump" role="img" aria-label="Photo of a blue industrial pump and pipework"></div>
    <svg class="footer-rule" viewBox="0 0 600 789" aria-hidden="true">
      <path d="M0 705 Q300 712 560 745" fill="none" stroke="var(--rule)" stroke-width="4"/>
    </svg>
    <div class="url-tab">www.korvanite.com.au</div>
  </section>

  <section class="page page--right">
    <div class="photo photo--refinery" role="img" aria-label="Photo of an oil refinery with towers, tanks and drums under a blue sky"></div>
    <div class="photo-band" style="top:430px;height:24px"></div>
    <div class="brand">
      <span class="brand-dot"></span>
      <span class="brand-name">Korvanite</span>
    </div>
    <div class="product-list">
      <h3>Composite hose</h3>
      <ul>
        <li>Stainless Steel Expansion Joints</li>
        <li>Rubber Expansion Joints</li>
        <li>Fabric Expansion Joints</li>
        <li>Hand Biuilt Rubber Hose</li>
        <li>Composite Ship To Shore Petroleum Dock Hose</li>
        <li>Stainless Braided Flexible Hose</li>
      </ul>
    </div>
    <div class="product-photo" role="img" aria-label="Product photo of a stainless steel bellows expansion joint with flanges"></div>
    <svg class="footer-rule" viewBox="0 0 600 789" aria-hidden="true">
      <path d="M20 705 Q300 712 590 752" fill="none" stroke="var(--rule)" stroke-width="4"/>
    </svg>
    <div class="url-tab">www.korvanite.com.au</div>
  </section>
</main>
</body>
</html>
```